Bahamas Pharmacy needs Flyer to Promote "Blood Pressure Tracking Service"

We need a double sided flyer design 5.5" x 8.5" (redesign) to promote a "Blood Pressure Tracking Service". Persons that have a card will be able to track their blood pressure online through a secure online blood pressure tracker. Clients of Brightwell Care Pharmacy will be to test themselves--so information is confidential. Test Regularly - their information is stored up to 30 readings. Share the printed results. Flyer must contain endorsement logos of Coral Reach Cardiac Association Flyer and Coral Reach Sugar Care Association. The final design should communicate responsible tracking of health of elders and parents look clean, crisp, elegant modern yet simplistic. Any imagery should be friendly to the mixed-race demographic of the Bahamas. Contain imagery on either side of "Chatterloop and Pipsqueal"

Target Market(s)

Families

Industry/Entity Type

Health

Font styles to use
Sans Serif

Colors
0255a3
9ccb3b
ffffff
ec2027

Requirements
Must have
• Images of Happy African-American or Mixed-Race Family, Similar Aesthetic to "Perks Circle" flyer
Nice to have
• Imagery of Nurse taking blood pressure monitor, please see example of imagery type to be used.
Should not have
• Too much text, Small Imagery,

```html
<!DOCTYPE html>
<html lang="en">
<head>
<meta charset="utf-8">
<title>Blood Pressure Tracking Service Flyers</title>
<link rel="stylesheet" href="https://fonts.googleapis.com/css2?family=Tinos:wght@400;700&display=swap">
<style>
  :root {
    --red: #ec2027;
    --red-deep: #c4161c;
    --blue: #0255a3;
    --blue-deep: #1c3f8a;
    --green: #9ccb3b;
    --white: #ffffff;
    --ink: #1f1f1f;
    --muted: #555555;
    --paper-bg: #ece6dd;
  }
  * { box-sizing: border-box; margin: 0; padding: 0; }
  html, body { width: 1200px; height: 728px; overflow: hidden; }
  body {
    background: var(--paper-bg);
    font-family: "Tinos", "Times New Roman", serif;
    color: var(--ink);
    position: relative;
  }
  .flyer {
    position: absolute;
    top: 24px;
    width: 440px;
    height: 680px;
    background: var(--white);
    overflow: hidden;
    box-shadow: 0 4px 14px rgba(0,0,0,0.12);
  }
  .flyer--elders { left: 140px; }
  .flyer--smart { left: 620px; }
  .shape { position: absolute; left: 0; width: 100%; display: block; }

  /* Shared brand line */
  .brand { position: absolute; display: flex; align-items: center; gap: 8px; }
  .brand-mark { width: 18px; height: 18px; border-radius: 50%; background: var(--red); flex: none; }
  .brand-name { color: var(--red); font-weight: 700; font-size: 18px; white-space: nowrap; }
  .brand-slogan { position: absolute; font-size: 11px; color: var(--muted); font-style: normal; white-space: nowrap; }

  /* ---------- Elders flyer ---------- */
  .elders-photo {
    position: absolute; left: 0; top: 90px; width: 100%; height: 300px;
    background: linear-gradient(135deg, #f4f4f2 0%, #dfe3e0 40%, #b9c7b4 70%, #8a8f95 100%);
  }
  .elders-banner { top: 0; height: 150px; }
  .elders-title {
    position: absolute; left: 28px; top: 26px; width: 300px;
    color: var(--white); font-weight: 700; font-size: 25px; line-height: 1.12;
  }
  .feature-list {
    position: absolute; left: 28px; top: 404px; width: 390px;
    display: grid; grid-template-columns: 120px 1fr; row-gap: 8px; column-gap: 10px;
  }
  .feature-list dt { color: var(--red); font-weight: 700; font-size: 15px; line-height: 1.15; }
  .feature-list dd { font-size: 14px; line-height: 1.2; }
  .flyer--elders .brand { left: 190px; top: 584px; }
  .flyer--elders .brand-slogan { left: 216px; top: 608px; }
  .elders-footer { bottom: 0; height: 56px; }

  /* ---------- Smart flyer ---------- */
  .smart-banner { top: 0; height: 96px; }
  .smart-title {
    position: absolute; left: 140px; top: 18px;
    color: var(--white); font-weight: 700; font-size: 44px; letter-spacing: 0.5px;
  }
  .flyer--smart .brand-top { left: 18px; top: 40px; }
  .service-line {
    position: absolute; left: 80px; top: 96px;
    color: var(--red); font-weight: 700; font-size: 19px;
  }
  .smart-photo {
    position: absolute; left: 0; top: 124px; width: 100%; height: 320px;
    background: linear-gradient(160deg, #e9ecef 0%, #cfd8de 35%, #b6c7d8 60%, #8c6a58 100%);
  }
  .smart-headline {
    position: absolute; left: 24px; top: 456px;
    color: var(--red); font-weight: 700; font-size: 34px; white-space: nowrap;
  }
  .smart-copy {
    position: absolute; left: 24px; top: 498px; width: 396px;
    font-size: 13px; line-height: 1.3; color: #333;
  }
  .smart-copy .hl { color: var(--red); font-weight: 700; }
  .rule-line {
    position: absolute; left: 24px; top: 552px; width: 392px; height: 2px; background: var(--red);
  }
  .rule-line::after {
    content: ""; position: absolute; right: -4px; top: -3px; width: 8px; height: 8px;
    border-radius: 50%; border: 1.5px solid var(--ink); background: var(--white);
  }
  .flyer--smart .brand-bottom { left: 150px; top: 566px; }
  .flyer--smart .brand-slogan-bottom { left: 176px; top: 590px; }
  .partner-badges { position: absolute; left: 360px; top: 588px; display: flex; gap: 8px; }
  .partner-badge { width: 18px; height: 18px; border-radius: 50%; background: #d8dde6; }
  .partner-badge--sugar { background: #e3c9cb; }
  .contact-line {
    position: absolute; left: 24px; top: 618px; width: 396px; text-align: right;
    font-size: 9px; color: #444;
  }
  .smart-footer { bottom: 0; height: 44px; }
</style>
</head>
<body>

  <section class="flyer flyer--elders">
    <div class="elders-photo" role="img" aria-label="Doctor checking an older woman's blood pressure at a kiosk"></div>
    <svg class="shape elders-banner" viewBox="0 0 440 150" preserveAspectRatio="none" aria-hidden="true">
      <path d="M0 0 H360 C355 50 330 90 300 110 C240 140 120 120 0 150 Z" fill="var(--red)"/>
      <path d="M0 150 C120 120 240 140 300 110 C330 90 355 50 360 0 H366 C362 55 336 98 304 116 C240 146 120 128 0 156 Z" fill="var(--red-deep)"/>
    </svg>
    <h1 class="elders-title">Healthy Tracking System for Health of Elders and Parents</h1>

    <dl class="feature-list">
      <dt>Online Blood Pressure Tracker:</dt>
      <dd>View your result online through a secure online blood pressure tracker</dd>
      <dt>Simple &amp; Easy:</dt>
      <dd>Test Yourself on the blood pressure kiosk</dd>
      <dt>Test Regularly:</dt>
      <dd>The card will store their information upto 30 readings. Share the printed results.</dd>
      <dt>Consult Doctor:</dt>
      <dd>Share the printed result with your doctor/pharmacist to help you manage your health</dd>
    </dl>

    <div class="brand">
      <span class="brand-mark"></span>
      <span class="brand-name">Brightwell Care Pharmacy</span>
    </div>
    <p class="brand-slogan">Caring close, costing less</p>

    <svg class="shape elders-footer" viewBox="0 0 440 56" preserveAspectRatio="none" aria-hidden="true">
      <path d="M0 36 C120 56 300 50 440 14 V56 H0 Z" fill="var(--red)"/>
    </svg>
  </section>

  <section class="flyer flyer--smart">
    <svg class="shape smart-banner" viewBox="0 0 440 96" preserveAspectRatio="none" aria-hidden="true">
      <path d="M120 0 H440 V70 C360 84 250 84 150 96 C130 70 125 30 120 0 Z" fill="var(--blue-deep)"/>
    </svg>
    <h2 class="smart-title">Be Smart !</h2>
    <div class="brand brand-top">
      <span class="brand-mark"></span>
    </div>
    <p class="service-line">Online Blood Pressure Tracking Service</p>

    <div class="smart-photo" role="img" aria-label="Nurse taking an older man's blood pressure at home"></div>

    <h2 class="smart-headline">Track Your Blood Pressure</h2>
    <p class="smart-copy">If You have Medical Card you can track your blood pressure online through a secure online blood pressure tracker. Customer of <span class="hl">Brightwell Care Pharmacy</span> can test themselves &ndash; and all information is confidential.</p>
    <div class="rule-line"></div>

    <div class="brand brand-bottom">
      <span class="brand-mark"></span>
      <span class="brand-name">Brightwell Care Pharmacy</span>
    </div>
    <p class="brand-slogan brand-slogan-bottom">Caring close, costing less</p>
    <div class="partner-badges">
      <span class="partner-badge" aria-label="Coral Reach Cardiac Association"></span>
      <span class="partner-badge partner-badge--sugar" aria-label="Coral Reach Sugar Care Association"></span>
    </div>
    <p class="contact-line">12 Harbour Lane, Unit 4, Seabreeze Plaza, Port Lucaya. Tel: 555-0142 Fax: 555-0143</p>

    <svg class="shape smart-footer" viewBox="0 0 440 44" preserveAspectRatio="none" aria-hidden="true">
      <path d="M0 10 C140 44 300 40 440 30 V44 H0 Z" fill="var(--blue)"/>
    </svg>
  </section>

</body>
</html>
```